Wandrift: Travel business card redesign

We need a clean elegant look for our cards featuring blue and orange. Look should communicate a sense of strong design and seem uncluttered. The company is Wandrift which means drift to wander. As in every trip is an drift to wander. Feel free to reinvent the logo or just tweak it. Colors should be blue like Caribbean waters and a saturated orange. Keep it clean and simple.
Please match the information in the sample uploaded but the sample is horrible -- a non-starter -- use for information only. also please add managing director to my name as title

Target Market(s)
potential clients, hotels, trade publications
Industry/Entity Type
Travel Industry
Contact Information for Business Card
as above
Requirements
Must have
- Font should be century gothic. Colors below are close but a but prefer lighter in each case.

```html
<!DOCTYPE html>
<html lang="en">
<head>
<meta charset="utf-8">
<title>Wandrift business cards</title>
<link rel="stylesheet" href="https://fonts.googleapis.com/css2?family=Didact+Gothic&display=swap">
<style>
  :root {
    --sea-blue: #62a9d3;
    --ink-blue: #4f9bcf;
    --sun-orange: #ef8a22;
    --paper: #ffffff;
    --backdrop: #e9ecef;
  }
  * { box-sizing: border-box; margin: 0; padding: 0; }
  html, body { width: 1200px; height: 864px; overflow: hidden; }
  body {
    background: var(--backdrop);
    font-family: "Didact Gothic", "Century Gothic", sans-serif;
    display: flex;
    align-items: center;
    justify-content: center;
    gap: 40px;
  }
  .card {
    position: relative;
    width: 540px;
    height: 309px;
    overflow: hidden;
    box-shadow: 0 6px 18px rgba(0,0,0,0.15);
  }
  .card--front { background: var(--sea-blue); color: var(--paper); }
  .card--back { background: var(--paper); }

  .wordmark { position: absolute; line-height: 1; }
  .wordmark__name { display: block; font-size: 62px; letter-spacing: -1px; }
  .wordmark__tagline { display: block; font-size: 22px; text-align: right; margin-top: 2px; }

  .card--front .wordmark { left: 0; right: 0; top: 92px; text-align: center; }
  .card--front .wordmark__tagline { text-align: center; padding-left: 160px; }
  .front__claim {
    position: absolute; left: 0; right: 0; bottom: 48px;
    text-align: center; font-size: 17px; line-height: 1.2; letter-spacing: 0.5px;
  }

  .card--back .wordmark { top: 28px; right: 34px; }
  .card--back .wordmark__name { font-size: 44px; color: var(--sun-orange); }
  .card--back .wordmark__tagline { font-size: 17px; color: var(--ink-blue); }

  .contact { position: absolute; left: 40px; bottom: 24px; color: var(--ink-blue); }
  .contact__name { color: var(--sun-orange); font-size: 26px; font-weight: 400; line-height: 1.2; }
  .contact__title { font-size: 13px; line-height: 1.3; letter-spacing: 0.5px; margin-bottom: 10px; }
  .contact__address { font-size: 15px; line-height: 1.25; margin-bottom: 8px; }
  .contact__list { list-style: none; font-size: 15px; line-height: 1.3; }
  .contact__list li { display: flex; align-items: center; gap: 8px; }
  .contact__icon { width: 13px; height: 13px; fill: var(--sun-orange); flex: none; }
</style>
</head>
<body>
  <section class="card card--front">
    <div class="wordmark">
      <span class="wordmark__name">Wandrift</span>
      <span class="wordmark__tagline">drift to wander</span>
    </div>
    <p class="front__claim">a first in service company</p>
  </section>

  <section class="card card--back">
    <div class="wordmark">
      <span class="wordmark__name">Wandrift</span>
      <span class="wordmark__tagline">drift to wander</span>
    </div>
    <div class="contact">
      <h1 class="contact__name">Leo Marrin</h1>
      <p class="contact__title">Managing Director</p>
      <p class="contact__address">1460 Harbor Crest Way N.<br>Seabright, 90277</p>
      <ul class="contact__list">
        <li><svg class="contact__icon" viewBox="0 0 16 16"><path d="M3 1l3 0 1 4-2 1.5c1 2 2.5 3.5 4.5 4.5L11 9l4 1v3c0 1-1 2-2 2C6 15 1 10 1 3c0-1 1-2 2-2z"/></svg>877.55.DRIFT (374384)</li>
        <li><svg class="contact__icon" viewBox="0 0 16 16"><path d="M4 0h8a1 1 0 0 1 1 1v14a1 1 0 0 1-1 1H4a1 1 0 0 1-1-1V1a1 1 0 0 1 1-1zm1 2v10h6V2zm3 11a1 1 0 1 0 0 2 1 1 0 0 0 0-2z"/></svg>323.555.0142</li>
        <li><svg class="contact__icon" viewBox="0 0 16 16"><path d="M0 3h16v10H0zm1.5 1L8 9l6.5-5z"/></svg>310.555.0187</li>
        <li><svg class="contact__icon" viewBox="0 0 16 16"><circle cx="8" cy="8" r="7" fill="none" stroke="#ef8a22" stroke-width="1.6"/><path d="M1 8h14M8 1c-3 3-3 11 0 14M8 1c3 3 3 11 0 14" fill="none" stroke="#ef8a22" stroke-width="1.4"/></svg>wandrift.example</li>
      </ul>
    </div>
  </section>
</body>
</html>
```